Marigold Haven - Foundation PPT

Design a cohesive, emotionally resonant PowerPoint template that reflects the heart of Marigold Haven Pregnancy & Family Support. This template will be used across fundraising, partnership, and storytelling presentations, and must balance professionalism with warmth, compassion, and human connection.

Background
Marigold Haven Pregnancy & Family Support exists to support families navigating complicated pregnancies, prolonged hospital stays, and loss. The brand is rooted in empathy, quiet strength, and the concept of a “web” of care—an interconnected support system that surrounds families during difficult moments.

The template should feel deeply personal and mission-driven, not corporate.

Design Goals
Create a visually cohesive slide system that can be reused across multiple presentation types

Capture the emotional tone of the organization:
-Warm
-Gentle
-Hopeful
-Supportive
Ensure the design is clean, minimal, and easy to use for non-designers
Maintain a balance between storytelling and credibility

Key Design Requirements
-Brand Integration: Incorporate the Marigold Haven logo (provided)
Align with soft, neutral color palette (e.g., cream, sage, blush, light sky tones)
-Use elegant, readable typography

Slide Templates to Include
-Cover Slide (emotion-forward, minimal text)
-Mission / Story Slide
-Program Overview Slide
-Impact / Metrics Slide
-Partnership / Sponsor Slide
-“Web of Support” Concept Slide (visual representation of interconnected care)
-Call to Action Slide
-Optional: Quote/Testimonial Slide

Visual Style
-Soft, calming, and approachable aesthetic
-Use of whitespace to avoid clutter
-Light use of icons or illustrations (if applicable)
-Avoid overly corporate or overly busy design elements

Usability
-Fully editable in PowerPoint
-Clear text hierarchy and placeholders
-Easy for internal team to update content without design support
-Tone & Emotional Direction

This is not a clinical or corporate presentation—it should feel human, heartfelt, and intentional.

website: https://www.marigoldhavencare.org

```html
<!DOCTYPE html>
<html lang="en">
<head>
<meta charset="utf-8">
<title>Marigold Haven – Foundation Presentation Template</title>
<link href="https://fonts.googleapis.com/css2?family=Dancing+Script:wght@500;600&family=Poppins:wght@400;500&display=swap" rel="stylesheet">
<style>
:root{
  --board:#808080;
  --purple:#9a61ac;
  --purple-soft:#f7eefb;
  --ink:#1f1f1f;
  --text:#6a6a6a;
  --white:#ffffff;
  --fog:#e8e8e9;
  --blush:#c99c9c;
  --script:"Dancing Script", cursive;
  --sans:"Poppins", sans-serif;
}
*{margin:0;padding:0;box-sizing:border-box}
html,body{width:1193px;height:1200px;overflow:hidden;background:var(--board)}
.board{position:relative;width:1193px;height:1200px;font-family:var(--sans)}

.slide{position:absolute;width:419px;height:236px;overflow:hidden;
  background:linear-gradient(180deg,var(--purple-soft) 0%,var(--white) 42%,var(--white) 60%,var(--fog) 100%);
  box-shadow:0 2px 6px rgba(0,0,0,.35)}
.col-a{left:134px}.col-b{left:593px}
.row-1{top:92px}.row-2{top:342px}.row-3{top:593px}.row-4{top:852px}

.abs{position:absolute}
.title{position:absolute;font-family:var(--script);font-weight:600;font-size:12.5px;color:var(--ink);white-space:nowrap}
.title .accent{color:var(--purple)}
.body{font-size:3.7px;line-height:7.8px;color:var(--text)}

.mini-logo{position:absolute;top:20px;right:20px;display:flex;align-items:center;gap:2px;color:var(--purple);font-weight:500}
.mini-logo .dot{width:7px;height:7px;border-radius:50%;background:var(--purple);opacity:.6}
.mini-logo .name{font-size:5.3px;line-height:5px;display:block}
.mini-logo .tag{font-size:2.4px;display:block}

.page{position:absolute;right:30px;bottom:14px;display:flex;align-items:center;gap:5px}
.page .word{font-family:var(--script);font-size:6.5px;color:var(--ink)}
.page .num{width:13px;height:13px;border-radius:50%;background:var(--purple);color:var(--white);font-size:5.5px;display:flex;align-items:center;justify-content:center}

/* cover */
.cover{background:linear-gradient(135deg,#9861ab,#9a63ae 60%,#9c67b0)}
.cover .corner-name{position:absolute;left:19px;top:23px;color:var(--white);font-weight:500;font-size:5px;line-height:5px}
.cover .corner-name small{display:block;font-size:2.4px}
.cover .lockup{position:absolute;left:20px;top:100px;display:flex;align-items:center;gap:8px;color:var(--white);font-weight:500}
.cover .lockup .dot{width:30px;height:30px;border-radius:50%;background:var(--white);opacity:.25}
.cover .lockup .name{display:block;font-size:23px;line-height:26px}
.cover .lockup .tag{display:block;font-size:7.8px;letter-spacing:.9px}

/* about */
.about .photo{left:197px;top:43px;width:222px;height:149px;border-radius:80px 0 0 80px/75px 0 0 75px;
  background:linear-gradient(180deg,#6f9a4f 0%,#a9c884 45%,#7e94b6 70%,#b5783f 100%)}

/* programs */
.program{position:absolute;width:113px;height:51px;background:var(--white);border-radius:3px;
  box-shadow:0 1px 4px rgba(0,0,0,.1);padding:6px 6px 0 6px}
.program h3{font-family:var(--script);font-weight:500;font-size:6.5px;color:var(--ink);margin-bottom:2px}
.program.accent h3{color:var(--purple)}
.program p{font-size:3.6px;line-height:7.6px;color:var(--text)}
.program .dots{position:absolute;right:14px;bottom:-1px;display:flex;gap:1px}
.program .dots i{width:4.5px;height:4.5px;border-radius:50%;border:1.1px solid var(--ink);background:var(--white)}
.program.accent .dots i{border-color:var(--purple)}

/* reach */
.reach .photo{left:0;top:0;width:171px;height:214px;border-radius:0 160px 160px 0/0 110px 110px 0;
  background:linear-gradient(160deg,#c07966 0%,#ad6d5c 55%,#8e5446 100%)}
.reach .title{left:200px;top:52px}
.reach .sub{position:absolute;left:205px;top:67px;width:110px;text-align:center;font-size:3.5px;color:var(--text)}
.stat{position:absolute;width:91px;height:40px;background:var(--white);border-radius:3px;box-shadow:0 1px 4px rgba(0,0,0,.1);text-align:center;padding-top:9px}
.stat b{display:block;font-family:var(--script);font-weight:500;font-size:15px;line-height:15px;color:var(--purple)}
.stat span{display:block;font-size:3.8px;color:var(--text)}

/* model */
.model .label{position:absolute;width:68px}
.model .label h4{font-family:var(--script);font-weight:500;font-size:5px;color:var(--purple)}
.model .label p{font-size:3px;line-height:4.6px;color:var(--text)}

/* partnership */
.tier .disc{position:absolute;width:28px;height:28px;border-radius:50%;background:var(--purple)}
.tier .copy{position:absolute;width:72px}
.tier h4{font-family:var(--script);font-weight:500;font-size:7px;color:var(--ink)}
.tier p{font-size:3.6px;line-height:5.5px;color:var(--text)}

/* testimonials */
.quote{position:absolute;width:155px;height:59px;background:var(--white);border-radius:3px;box-shadow:0 1px 4px rgba(0,0,0,.1);padding:8px 8px 0 8px}
.quote .mark{position:absolute;left:5px;top:-2px;font-family:Georgia,serif;font-size:22px;color:#e6e6e6}
.quote p{position:relative;font-size:3.6px;line-height:7.8px;color:var(--text)}
.quote .who{position:absolute;right:10px;bottom:8px;font-family:var(--script);font-weight:500;font-size:6.5px;color:var(--ink)}

/* thank you */
.thanks .blush{position:absolute;border-radius:50%;background:var(--blush)}
.thanks .photo{left:192px;top:15px;width:204px;height:204px;border-radius:50%;
  background:linear-gradient(150deg,#f1f0ee 0%,#d9dcd6 40%,#93a47a 75%,#7d8a6c 100%)}
.thanks .lockup{position:absolute;left:19px;top:18px;display:flex;align-items:center;gap:4px;color:var(--purple);font-weight:500}
.thanks .lockup .dot{width:16px;height:16px;border-radius:50%;background:var(--purple);opacity:.35}
.thanks .lockup .name{display:block;font-size:12px;line-height:13px}
.thanks .lockup .tag{display:block;font-size:4.4px;letter-spacing:.4px}
.thanks .title{left:19px;top:66px}
.thanks .sub{position:absolute;left:19px;top:84px;font-size:4.3px;color:var(--text)}
.contact{position:absolute;left:19px;top:106px;width:227px;height:90px;background:var(--white);border-radius:4px;box-shadow:0 1px 5px rgba(0,0,0,.1)}
.contact .item{position:absolute;display:flex;gap:4px}
.contact svg{flex:none}
.contact h5{font-family:var(--script);font-weight:500;font-size:7px;color:var(--ink);line-height:8px}
.contact p{font-size:4.4px;color:var(--text);line-height:5.8px}
.contact p.big{font-size:6px}
</style>
</head>
<body>
<main class="board">

  <!-- Cover -->
  <section class="slide cover col-a row-1">
    <div class="corner-name">Marigold Haven<small>Pregnancy &amp; Family Support</small></div>
    <div class="lockup">
      <span class="dot"></span>
      <div><span class="name">Marigold Haven</span><span class="tag">Pregnancy &amp; Family Support</span></div>
    </div>
  </section>

  <!-- About -->
  <section class="slide about col-b row-1">
    <div class="mini-logo"><span class="dot"></span><div><span class="name">Marigold Haven</span><span class="tag">Pregnancy &amp; Family Support</span></div></div>
    <h2 class="title" style="left:19px;top:40px">About <span class="accent">Marigold Haven</span></h2>
    <p class="body abs" style="left:19px;top:59px;width:148px">Lorem ipsum dolor sit amet, consectetuer adipiscing elit, sed diam nonummy nibh euismod tincidunt ut laoreet dolore magna aliquam erat volutpat. Ut wisi enim ad minim veniam, quis nostrud exerci tation ullamcorper suscipit lobortis nisl ut aliquip ex ea commodo consequat. Duis autem vel eum iriure dolor in hendrerit in vulputate velit esse molestie consequat, vel illum dolore eu feugiat nulla facilisis at vero eros et accumsan et iusto odio dignissim qui blandit praesent luptatum zzril delenit augue duis dolore te feugait nulla facilisi.<br>Lorem ipsum dolor sit amet, cons ectetuer adipiscing elit, sed diam nonummy nibh euismod tincidunt ut laoreet dolore magna aliquam erat volutpat. Ut wisi enim ad minim veniam, quis nostrud exerci tation ullamcorper suscipit lobortis nisl ut aliquip ex ea commodo consequat.</p>
    <div class="photo abs" role="img" aria-label="Photo of a couple sitting close together on a park bench"></div>
    <div class="page"><span class="word">Page</span><span class="num">1</span></div>
  </section>

  <!-- Programs -->
  <section class="slide programs col-a row-2">
    <div class="mini-logo"><span class="dot"></span><div><span class="name">Marigold Haven</span><span class="tag">Pregnancy &amp; Family Support</span></div></div>
    <h2 class="title" style="left:20px;top:36px"><span class="accent">Our</span> Programs</h2>
    <article class="program accent" style="left:20px;top:57px"><h3>Program One</h3><p>Lorem ipsum dolor sit amet, consectetuer adipiscing elit, sed diam nonummy nibh euismod tincidunt ut laoreet</p><div class="dots"><i></i><i></i><i></i></div></article>
    <article class="program" style="left:149px;top:57px"><h3>Program One</h3><p>Lorem ipsum dolor sit amet, consectetuer adipiscing elit, sed diam nonummy nibh euismod tincidunt ut laoreet</p><div class="dots"><i></i><i></i><i></i></div></article>
    <article class="program accent" style="left:278px;top:57px"><h3>Program One</h3><p>Lorem ipsum dolor sit amet, consectetuer adipiscing elit, sed diam nonummy nibh euismod tincidunt ut laoreet</p><div class="dots"><i></i><i></i><i></i></div></article>
    <article class="program" style="left:20px;top:120px"><h3>Program One</h3><p>Lorem ipsum dolor sit amet, consectetuer adipiscing elit, sed diam nonummy nibh euismod tincidunt ut laoreet</p><div class="dots"><i></i><i></i><i></i></div></article>
    <article class="program accent" style="left:149px;top:120px"><h3>Program One</h3><p>Lorem ipsum dolor sit amet, consectetuer adipiscing elit, sed diam nonummy nibh euismod tincidunt ut laoreet</p><div class="dots"><i></i><i></i><i></i></div></article>
    <article class="program" style="left:278px;top:120px"><h3>Program One</h3><p>Lorem ipsum dolor sit amet, consectetuer adipiscing elit, sed diam nonummy nibh euismod tincidunt ut laoreet</p><div class="dots"><i></i><i></i><i></i></div></article>
    <div class="page"><span class="word">Page</span><span class="num">2</span></div>
  </section>

  <!-- Reach -->
  <section class="slide reach col-b row-2">
    <div class="photo abs" role="img" aria-label="Photo of a wall of framed black-and-white family portraits"></div>
    <div class="mini-logo"><span class="dot"></span><div><span class="name">Marigold Haven</span><span class="tag">Pregnancy &amp; Family Support</span></div></div>
    <h2 class="title"><span class="accent">Our Reach,</span> Our Results</h2>
    <p class="sub">IN POST-PROGRAM FOLLOW-UP SURVEYS</p>
    <div class="stat" style="left:155px;top:85px"><b>3,800+</b><span>Mothers Supported</span></div>
    <div class="stat" style="left:266px;top:85px"><b>6+ Active</b><span>Program Pillars</span></div>
    <div class="stat" style="left:210px;top:140px"><b>91%</b><span>Reported Feeling Less Alone</span></div>
    <div class="page"><span class="word">Page</span><span class="num">3</span></div>
  </section>

  <!-- Model -->
  <section class="slide model col-a row-3">
    <div class="mini-logo"><span class="dot"></span><div><span class="name">Marigold Haven</span><span class="tag">Pregnancy &amp; Family Support</span></div></div>
    <h2 class="title" style="left:22px;top:40px">The <span class="accent">Marigold Haven</span> Model</h2>
    <svg class="abs" style="left:0;top:0" width="419" height="236" viewBox="0 0 419 236" aria-hidden="true">
      <g stroke="#c9b3d1" stroke-width=".6" fill="none">
        <path d="M92 79V126H303V79"/><path d="M197 79V126"/><path d="M146 126V174"/><path d="M250 126V174"/>
      </g>
      <g fill="#9a61ac">
        <polygon points="92,65 104,72 104,86 92,93 80,86 80,72"/>
        <polygon points="303,65 315,72 315,86 303,93 291,86 291,72"/>
        <polygon points="146,160 158,167 158,181 146,188 134,181 134,167"/>
        <polygon points="250,160 262,167 262,181 250,188 238,181 238,167"/>
        <circle cx="146" cy="126" r="1.5"/><circle cx="250" cy="126" r="1.5"/><circle cx="303" cy="126" r="1.5"/>
      </g>
      <polygon fill="#1f1f1f" points="197,65 209,72 209,86 197,93 185,86 185,72"/>
      <circle fill="#1f1f1f" cx="197" cy="126" r="1.5"/>
    </svg>
    <div class="label" style="left:112px;top:69px"><h4>Insert Tittle Here</h4><p>Lorem ipsum dolor sit amet, consectetuer adipiscing elit, sed diam nonummy nibh euismod tincidunt ut</p></div>
    <div class="label" style="left:219px;top:69px"><h4>Insert Tittle Here</h4><p>Lorem ipsum dolor sit amet, consectetuer adipiscing elit, sed diam nonummy nibh euismod tincidunt ut</p></div>
    <div class="label" style="left:71px;top:141px"><h4>Insert Tittle Here</h4><p>Lorem ipsum dolor sit amet, consectetuer adipiscing elit, sed diam nonummy nibh euismod tincidunt ut</p></div>
    <div class="label" style="left:171px;top:141px"><h4>Insert Tittle Here</h4><p>Lorem ipsum dolor sit amet, consectetuer adipiscing elit, sed diam nonummy nibh euismod tincidunt ut</p></div>
    <div class="label" style="left:271px;top:141px"><h4>Insert Tittle Here</h4><p>Lorem ipsum dolor sit amet, consectetuer adipiscing elit, sed diam nonummy nibh euismod tincidunt ut</p></div>
    <div class="page"><span class="word">Page</span><span class="num">4</span></div>
  </section>

  <!-- Partnership -->
  <section class="slide partners col-b row-3">
    <div class="mini-logo"><span class="dot"></span><div><span class="name">Marigold Haven</span><span class="tag">Pregnancy &amp; Family Support</span></div></div>
    <h2 class="title" style="left:19px;top:54px"><span class="accent">Partnership</span> / Sponsor</h2>
    <div class="tier"><span class="disc" style="left:21px;top:87px"></span><div class="copy" style="left:65px;top:87px"><h4>Tier One</h4><p>Lorem ipsum dolor sit amet, consectetuer adipiscing elit, sed diam nonummy nibh euismod tincidu</p></div></div>
    <div class="tier"><span class="disc" style="left:192px;top:87px"></span><div class="copy" style="left:235px;top:87px"><h4>Tier One</h4><p>Lorem ipsum dolor sit amet, consectetuer adipiscing elit, sed diam nonummy nibh euismod tincidu</p></div></div>
    <div class="tier"><span class="disc" style="left:21px;top:140px"></span><div class="copy" style="left:65px;top:138px"><h4>Tier One</h4><p>Lorem ipsum dolor sit amet, consectetuer adipiscing elit, sed diam nonummy nibh euismod tincidu</p></div></div>
    <div class="tier"><span class="disc" style="left:192px;top:140px"></span><div class="copy" style="left:235px;top:138px"><h4>Tier One</h4><p>Lorem ipsum dolor sit amet, consectetuer adipiscing elit, sed diam nonummy nibh euismod tincidu</p></div></div>
    <div class="page"><span class="word">Page</span><span class="num">5</span></div>
  </section>

  <!-- Testimonials -->
  <section class="slide words col-a row-4">
    <div class="mini-logo"><span class="dot"></span><div><span class="name">Marigold Haven</span><span class="tag">Pregnancy &amp; Family Support</span></div></div>
    <h2 class="title" style="left:20px;top:35px"><span class="accent">In</span> Their Own Words</h2>
    <blockquote class="quote" style="left:20px;top:57px"><span class="mark">“</span><p>Lorem ipsum dolor sit amet, consectetuer adipiscing elit, sed diam nonummy nibh euismod tincidunt ut laoreet dolore magna aliquam erat Lorem ipsum dolor sit amet, consectetuer adipiscing elit, sed diam nonummy nibh</p><cite class="who">Name Here</cite></blockquote>
    <blockquote class="quote" style="left:202px;top:57px"><span class="mark">“</span><p>Lorem ipsum dolor sit amet, consectetuer adipiscing elit, sed diam nonummy nibh euismod tincidunt ut laoreet dolore magna aliquam erat Lorem ipsum dolor sit amet, consectetuer adipiscing elit, sed diam nonummy nibh</p><cite class="who">Name Here</cite></blockquote>
    <blockquote class="quote" style="left:20px;top:124px"><span class="mark">“</span><p>Lorem ipsum dolor sit amet, consectetuer adipiscing elit, sed diam nonummy nibh euismod tincidunt ut laoreet dolore magna aliquam erat Lorem ipsum dolor sit amet, consectetuer adipiscing elit, sed diam nonummy nibh</p><cite class="who">Name Here</cite></blockquote>
    <blockquote class="quote" style="left:202px;top:124px"><span class="mark">“</span><p>Lorem ipsum dolor sit amet, consectetuer adipiscing elit, sed diam nonummy nibh euismod tincidunt ut laoreet dolore magna aliquam erat Lorem ipsum dolor sit amet, consectetuer adipiscing elit, sed diam nonummy nibh</p><cite class="who">Name Here</cite></blockquote>
    <div class="page"><span class="word">Page</span><span class="num">6</span></div>
  </section>

  <!-- Thank you -->
  <section class="slide thanks col-b row-4">
    <span class="blush" style="left:355px;top:-2px;width:80px;height:80px"></span>
    <span class="blush" style="left:0;top:180px;width:64px;height:64px"></span>
    <div class="photo abs" role="img" aria-label="Photo of a woman opening white curtains to a bright window, seen from behind"></div>
    <div class="lockup"><span class="dot"></span><div><span class="name">Marigold Haven</span><span class="tag">Pregnancy &amp; Family Support</span></div></div>
    <h2 class="title"><span class="accent">Thank</span> You</h2>
    <p class="sub">ASK US FOR ADVICE NOW</p>
    <div class="contact">
      <div class="item" style="left:11px;top:16px">
        <svg width="13" height="13" viewBox="0 0 13 13" aria-hidden="true"><circle cx="6.5" cy="6.5" r="6" fill="none" stroke="#9a61ac" stroke-width=".6"/><path d="M4.3 3.6l1.2-.3.7 1.6-.8.6a4.3 4.3 0 0 0 2 2l.6-.8 1.6.7-.3 1.2c-2.8.2-5.2-2.2-5-5z" fill="none" stroke="#9a61ac" stroke-width=".6"/></svg>
        <div><h5>Phone Number</h5><p class="big">013 555 0190</p></div>
      </div>
      <div class="item" style="left:108px;top:16px">
        <svg width="13" height="13" viewBox="0 0 13 13" aria-hidden="true"><circle cx="6.5" cy="6.5" r="6" fill="none" stroke="#9a61ac" stroke-width=".6"/><rect x="3.6" y="4.5" width="5.8" height="4" fill="#9a61ac"/><path d="M3.6 4.6l2.9 2.2 2.9-2.2" fill="none" stroke="#fff" stroke-width=".5"/></svg>
        <div><h5>Email</h5><p>hello@marigoldhavencare.org</p></div>
      </div>
      <div class="item" style="left:11px;top:50px">
        <svg width="13" height="13" viewBox="0 0 13 13" aria-hidden="true"><circle cx="6.5" cy="6.5" r="6" fill="none" stroke="#9a61ac" stroke-width=".6"/><circle cx="6.5" cy="6.5" r="3.2" fill="none" stroke="#9a61ac" stroke-width=".6"/><path d="M3.3 6.5h6.4M6.5 3.3c-1.6 2-1.6 4.4 0 6.4M6.5 3.3c1.6 2 1.6 4.4 0 6.4" fill="none" stroke="#9a61ac" stroke-width=".5"/></svg>
        <div><h5>Website</h5><p>www.marigoldhavencare.org</p></div>
      </div>
      <div class="item" style="left:108px;top:50px">
        <svg width="13" height="13" viewBox="0 0 13 13" aria-hidden="true"><circle cx="6.5" cy="6.5" r="6" fill="none" stroke="#9a61ac" stroke-width=".6"/><path d="M6.5 10S4.2 7.4 4.2 5.6a2.3 2.3 0 0 1 4.6 0C8.8 7.4 6.5 10 6.5 10z" fill="none" stroke="#9a61ac" stroke-width=".6"/><circle cx="6.5" cy="5.6" r=".8" fill="#9a61ac"/></svg>
        <div><h5>Office Address</h5><p>Lorem Lorem ipsum dolor sit<br>amet, consectetuer</p></div>
      </div>
    </div>
  </section>

</main>
</body>
</html>
```